Hollowmere Dental Center Specials/Offers

Take the advertisement pic (LABELED ADVERTISEMENT) and make it look "professional in appearance" using the logo and color scheme of Hollowmere Dental Center. The Phone number should be 719-555-0186. I want the same content, different background, professional looking document. I want it to be a 12"x12" document. High resolution files should include .PDF, .JPG and .AI. Any or all documents can be used for colors and overall scheme. I would like to have the overall colors include the main blue color from the file 4db749b4ef4c5e0717512bf7eb26bf54 and include the brown "swoosh" somewhere through/on the final document. Stock files of smiling young families can be used but not required. I am on a tight time-line and have placed 5 days as the deadline, but I will pick my favorite in as little as 2-3 days if I can get a good product. Again ALL the info from the Advertisement document should be included on the final product. Use any or all of the uploaded files for assistance. You can also visit our website for more info: www.hollowmeredentalcenter.example Thanks

```html
<!DOCTYPE html>
<html lang="en">
<head>
<meta charset="utf-8">
<title>Hollowmere Dental Center – Specials &amp; Offers</title>
<link rel="stylesheet" href="https://fonts.googleapis.com/css2?family=Montserrat:wght@400;500;600&family=Open+Sans:ital,wght@0,400;0,600;1,400&display=swap">
<style>
  :root {
    --teal: #6fa8b4;
    --teal-soft: #7db1bc;
    --cocoa: #3e3437;
    --cocoa-soft: #4a3f42;
    --ink: #3a3a3a;
    --paper: #ffffff;
    --white: #ffffff;
  }
  * { box-sizing: border-box; margin: 0; padding: 0; }
  html, body { width: 1200px; height: 1200px; overflow: hidden; background: var(--paper); }
  .ad { position: relative; width: 1200px; height: 1200px; background: var(--paper); font-family: "Open Sans", Arial, sans-serif; color: var(--white); }
  .tile { position: absolute; border-radius: 10px; }
  .tile--teal { background: var(--teal); }
  .tile--cocoa { background: var(--cocoa); }

  .brand { left: 38px; top: 30px; width: 477px; height: 271px; background: var(--paper); border: 2px solid var(--cocoa); display: flex; align-items: center; justify-content: center; gap: 20px; padding: 0 30px; }
  .brand__dot { width: 46px; height: 46px; border-radius: 50%; background: var(--teal); flex: none; }
  .brand__name { font-family: "Montserrat", Arial, sans-serif; font-weight: 500; font-size: 36px; line-height: 1.15; color: var(--cocoa); }

  .tagline { left: 552px; top: 30px; width: 612px; height: 271px; }
  .tagline__text { position: absolute; top: 64px; left: 0; right: 0; text-align: center; font-family: "Montserrat", Arial, sans-serif; font-weight: 600; font-size: 38px; line-height: 1.45; letter-spacing: 0.3px; }

  .ornament-area { position: absolute; background: var(--teal-soft); }
  .tile--cocoa .ornament-area { background: var(--cocoa-soft); }

  .providers { left: 38px; top: 349px; width: 477px; height: 325px; padding: 50px 0 0 8px; font-weight: 600; font-size: 24px; line-height: 1.4; white-space: nowrap; }
  .providers p + p { margin-top: 32px; }

  .new-patient { left: 552px; top: 347px; width: 612px; height: 325px; text-align: center; padding-top: 30px; font-weight: 600; font-size: 28px; line-height: 1.47; }
  .note { font-weight: 400; font-style: italic; font-size: 21px; }
  .new-patient .note { margin-top: 40px; }

  .referral { left: 38px; top: 714px; width: 228px; height: 326px; padding: 122px 0 0 16px; font-size: 23px; line-height: 1.45; }
  .first-visit { left: 292px; top: 714px; width: 620px; height: 326px; padding: 34px 0 0 72px; font-family: "Montserrat", Arial, sans-serif; font-weight: 600; }
  .first-visit__pct { display: block; font-size: 40px; padding-left: 66px; }
  .first-visit__title { display: block; font-size: 44px; line-height: 1.45; margin-top: 0; }
  .first-visit .note { font-family: "Open Sans", Arial, sans-serif; margin-top: 24px; }
  .bleaching { left: 940px; top: 714px; width: 225px; height: 326px; padding: 122px 0 0 16px; font-size: 23px; line-height: 1.45; }

  .contact { position: absolute; left: 37px; top: 1072px; width: 1128px; height: 87px; border: 2px solid var(--cocoa); border-radius: 8px; padding: 2px 0 0 40px; }
  .contact__call { font-family: "Montserrat", Arial, sans-serif; font-weight: 500; font-size: 40px; color: var(--ink); display: flex; justify-content: space-between; padding-right: 20px; line-height: 1.2; }
  .contact__web { font-style: italic; font-size: 26px; color: var(--teal); line-height: 1.2; }
</style>
</head>
<body>
<main class="ad">
  <div class="tile brand">
    <span class="brand__dot"></span>
    <span class="brand__name">Hollowmere Dental Center</span>
  </div>

  <section class="tile tile--teal tagline">
    <h1 class="tagline__text">WHERE THE WHOLE FAMILY<br>CAN BE SEEN</h1>
    <div class="ornament-area" role="img" aria-label="Decorative white leaf ornament" style="right:16px; bottom:16px; width:110px; height:84px;"></div>
  </section>

  <section class="tile tile--teal providers">
    <p>Preferred Provider For:</p>
    <p>Vela Dental, Metwell, Corva, Aldena<br>BlueCrest and United Harmonia</p>
    <p>We take all other non-HMO plans</p>
  </section>

  <section class="tile tile--teal new-patient">
    <p>$59 New patients<br>X-rays<br>Comprehensive Exam<br>Regular Cleaning</p>
    <p class="note">*Only patients without Dental Benefits</p>
  </section>

  <section class="tile tile--cocoa referral">
    <p>Ask about our<br>Referral Program</p>
    <div class="ornament-area" role="img" aria-label="Decorative white leaf ornament" style="right:16px; bottom:16px; width:68px; height:52px;"></div>
  </section>

  <section class="tile tile--teal first-visit">
    <span class="first-visit__pct">20% OFF</span>
    <span class="first-visit__title">Treatment scheduled<br>on your first visit.</span>
    <p class="note">*Only patients without Dental Benefits</p>
  </section>

  <section class="tile tile--cocoa bleaching">
    <p>$99<br>Bleaching Special</p>
    <div class="ornament-area" role="img" aria-label="Decorative white leaf ornament" style="right:16px; bottom:16px; width:68px; height:52px;"></div>
  </section>

  <footer class="contact">
    <p class="contact__call"><span>Call Today for an Appointment</span><span>719-555-0186</span></p>
    <p class="contact__web">www.hollowmeredentalcenter.example</p>
  </footer>
</main>
</body>
</html>
```